Meadowlark Dental Letterhead

Please design full color letterhead for meadowlark dental. Letterhead should match the motif of the business card. Print and logo should be confined to a one inch margin on top and bottom. The following info should be included:
Medowlark Dental with the tooth logo
Curtis L. Ferrell, DDS
Gentle Hands Always, Friendly Faces Daily
Phone #: 555.276.4158
Address: 20354-C N Larkspur, Bixby, OK

```html
<!DOCTYPE html>
<html lang="en">
<head>
<meta charset="utf-8">
<title>Meadowlark Dental Letterhead</title>
<link href="https://fonts.googleapis.com/css2?family=Montserrat:wght@500;600;700&family=Quicksand:wght@500&display=swap" rel="stylesheet">
<style>
  :root {
    --backdrop: #5e5e5e;
    --paper: #ffffff;
    --ink: #1f2a30;
    --brand-blue: #1f5fae;
    --brand-green: #4cb648;
    --watermark: #ecedec;
  }
  html, body {
    margin: 0;
    width: 1200px;
    height: 1000px;
    overflow: hidden;
    background: var(--backdrop);
  }
  .letterhead {
    position: absolute;
    left: 237px;
    top: 23px;
    width: 733px;
    height: 949px;
    background: var(--paper);
    overflow: hidden;
  }
  .brand {
    position: absolute;
    left: 52px;
    top: 29px;
    width: 126px;
    text-align: center;
  }
  .brand-square {
    display: block;
    width: 46px;
    height: 46px;
    margin: 0 auto 7px;
    background: var(--brand-green);
    border-radius: 4px;
  }
  .brand-name {
    margin: 0;
    font-family: "Montserrat", sans-serif;
    font-weight: 600;
    color: var(--brand-blue);
  }
  .brand-name span { display: block; }
  .brand-name .line-1 { font-size: 16.5px; line-height: 19px; letter-spacing: -0.3px; }
  .brand-name .line-2 { font-size: 17px; line-height: 19px; letter-spacing: 4px; padding-left: 4px; }
  .practice {
    position: absolute;
    right: 224px;
    top: 39px;
    text-align: right;
  }
  .tagline {
    margin: 0;
    font-family: "Montserrat", sans-serif;
    font-weight: 600;
    font-size: 7.5px;
    color: var(--ink);
    text-transform: uppercase;
  }
  .dentist {
    margin: 1px 0 0;
    font-family: "Montserrat", sans-serif;
    font-weight: 700;
    font-size: 12.5px;
    color: var(--brand-blue);
  }
  .contact {
    position: absolute;
    left: 523px;
    top: 37px;
    margin: 0;
    padding: 0;
    list-style: none;
    font-family: "Quicksand", sans-serif;
    font-weight: 500;
    color: var(--ink);
  }
  .contact li {
    display: flex;
    align-items: center;
    gap: 6px;
    height: 15px;
  }
  .contact .phone { font-size: 12px; }
  .contact .web { font-size: 11px; }
  .contact svg { width: 9px; height: 9px; flex: none; }
  .watermark {
    position: absolute;
    left: 249px;
    top: 372px;
    width: 236px;
    height: 236px;
    border-radius: 14px;
    background: var(--watermark);
  }
  .footer-rule {
    position: absolute;
    left: 0;
    bottom: 35px;
    width: 733px;
    height: 4px;
    background: var(--brand-blue);
  }
  .footer-band {
    position: absolute;
    left: 0;
    bottom: 0;
    width: 733px;
    height: 30px;
    background: var(--brand-green);
  }
  .address {
    position: absolute;
    right: 44px;
    bottom: 8px;
    margin: 0;
    font-family: "Quicksand", sans-serif;
    font-weight: 500;
    font-size: 12px;
    color: var(--paper);
  }
</style>
</head>
<body>
  <main class="letterhead">
    <header>
      <div class="brand">
        <span class="brand-square"></span>
        <p class="brand-name"><span class="line-1">MEADOWLARK</span><span class="line-2">DENTAL</span></p>
      </div>
      <div class="practice">
        <p class="tagline">Gentle Hands Always, Friendly Faces Daily</p>
        <p class="dentist">Curtis L. Ferrell, D.D.S.</p>
      </div>
      <ul class="contact">
        <li class="phone">
          <svg viewBox="0 0 10 10" aria-hidden="true"><rect x="0.5" y="0.5" width="9" height="9" rx="2" fill="var(--brand-blue)"/><path d="M3 3h4v1.2H3zM3.6 5h2.8v2H3.6z" fill="#fff"/></svg>
          555-276-4158
        </li>
        <li class="web">
          <svg viewBox="0 0 10 10" aria-hidden="true"><rect x="0.5" y="0.5" width="9" height="9" rx="2" fill="var(--brand-blue)"/><circle cx="5" cy="5" r="2.6" fill="none" stroke="#fff" stroke-width="0.9"/></svg>
          www.meadowlarkdentalok.com
        </li>
      </ul>
    </header>

    <div class="watermark" aria-hidden="true"></div>

    <footer>
      <div class="footer-rule" aria-hidden="true"></div>
      <div class="footer-band" aria-hidden="true"></div>
      <p class="address">20354-C North Larkspur, Millbrook, OK 74500</p>
    </footer>
  </main>
</body>
</html>
```